Vehicle graphics for healthcare company (bramblecovecare.co.uk)

I have a plain white van that needs some branding. I don't mind leaving a bit of the white, so I would consider a half wrap, or large panels of non-white, but I'm open to suggestion.

For a non-wrap design, I happened to see the KDT Van (attached photo), which I thought was a nice clear design. I thought maybe some elements of this could be included. Maybe their large A could be the S of my Bramble Cove logo.

The only two colours the company has used to date are the green and grey of the logo. 1B7F8C and 58585A.

The core business we provide is assessment for people about to purchase a wheelchair. We take their measurements, look at their clinical needs and then recommend a product for them to purchase.

The information we need on it:
- our logo (attached)
- Private Wheelchair Assessment
- Occupational Therapy
- Wheelchair Skills

Our contact details to be included:
- www.bramblecovecare.co.uk
- info@bramblecovecare.co.uk
- 02937 418205

Target Market(s)

Wheelchair users and other healthcare providers.

Industry/Entity Type

Healthcare

Font styles to use
Other font styles liked:
• Arthaus Medium

Requirements
Must have
• Logo, contact details. Green/grey colours. 1B7F8C and 58585A
Nice to have
• See attached van, I thought this was a simple, clear design.
Should not have
• Clutter.

```html
<!DOCTYPE html>
<html lang="en">
<head>
<meta charset="utf-8">
<title>Bramble Cove Therapy – Van Livery</title>
<link rel="stylesheet" href="https://fonts.googleapis.com/css2?family=Comfortaa:wght@500;700&display=swap">
<style>
  :root {
    --teal: #1B7F8C;
    --grey: #58585A;
    --panel: #ffffff;
    --panel-edge: #d9dcdd;
    --spine: #e9f3f4;
    --white: #ffffff;
  }
  html, body {
    margin: 0;
    padding: 0;
    width: 1200px;
    height: 674px;
    overflow: hidden;
    background: var(--white);
    font-family: "Comfortaa", sans-serif;
  }
  .livery { position: relative; width: 1200px; height: 674px; }
  .livery-side, .livery-rear { position: absolute; display: block; }
  .livery-side--driver { left: 40px; top: 30px; width: 730px; height: 300px; }
  .livery-side--passenger { left: 25px; top: 365px; width: 740px; height: 300px; }
  .livery-rear { left: 830px; top: 210px; width: 350px; height: 310px; }
  .panel-fill { fill: var(--panel); }
  .panel-frame { fill: none; stroke: var(--panel-edge); stroke-width: 2; }
  .band { fill: var(--teal); }
  .spine { fill: var(--spine); }
  .brand-name { font-family: "Comfortaa", sans-serif; font-weight: 700; fill: var(--teal); }
  .service-list { font-family: "Comfortaa", sans-serif; font-weight: 500; fill: var(--white); font-size: 11.5px; }
  .contact { font-family: "Comfortaa", sans-serif; font-weight: 700; fill: var(--teal); }
  .contact--small { font-size: 12px; }
  .contact--phone { font-size: 18px; }
  .rear-phone { font-family: "Comfortaa", sans-serif; font-weight: 700; fill: var(--white); font-size: 15px; }
  .tick { fill: none; stroke: var(--white); stroke-width: 1.4; }
</style>
</head>
<body>
<main class="livery">

  <!-- Driver side: front faces left -->
  <svg class="livery-side livery-side--driver" viewBox="0 0 730 300" aria-label="Driver side livery panel">
    <defs>
      <clipPath id="clip-driver"><rect x="10" y="10" width="710" height="270" rx="40"/></clipPath>
    </defs>
    <rect class="panel-fill" x="10" y="10" width="710" height="270" rx="40"/>
    <g clip-path="url(#clip-driver)">
      <path class="band" d="M230 290 C250 240 300 225 360 225 L730 212 L730 290 Z"/>
      <path class="band" d="M325 0 L395 0 C360 90 380 150 440 200 C480 235 470 265 450 290 L370 290 C400 240 380 210 350 170 C310 120 300 70 325 0 Z"/>
      <path class="spine" role="img" aria-label="Stylised white spine illustration sweeping down the side"
        d="M360 0 L392 0 C372 90 392 150 440 205 C470 240 440 265 400 290 L362 290 C405 250 420 225 395 190 C350 135 345 80 360 0 Z"/>
      <rect class="band" x="470" y="148" width="260" height="60" transform="rotate(-2 470 148)"/>
      <g class="service-list" transform="rotate(-2 490 165)">
        <path class="tick" d="M492 160 l3 3 l6 -7"/><text x="505" y="164">Private Wheelchair Assessment</text>
        <path class="tick" d="M492 177 l3 3 l6 -7"/><text x="505" y="181">Occupational Therapy</text>
        <path class="tick" d="M492 194 l3 3 l6 -7"/><text x="505" y="198">Wheelchair Skills</text>
      </g>
    </g>
    <rect class="panel-frame" x="10" y="10" width="710" height="270" rx="40"/>
    <text class="brand-name" x="520" y="80" font-size="40">Bramble</text>
    <text class="brand-name" x="522" y="112" font-size="19">Cove Therapy</text>
    <g transform="rotate(-4 300 200)" text-anchor="end">
      <text class="contact contact--small" x="312" y="180">info@bramblecovecare.co.uk</text>
      <text class="contact contact--small" x="312" y="198">bramblecovecare.co.uk</text>
      <text class="contact contact--phone" x="312" y="222">02937 418205</text>
    </g>
  </svg>

  <!-- Passenger side: front faces right -->
  <svg class="livery-side livery-side--passenger" viewBox="0 0 740 300" aria-label="Passenger side livery panel">
    <defs>
      <clipPath id="clip-passenger"><rect x="10" y="10" width="720" height="270" rx="40"/></clipPath>
    </defs>
    <rect class="panel-fill" x="10" y="10" width="720" height="270" rx="40"/>
    <g clip-path="url(#clip-passenger)">
      <path class="band" d="M0 290 L0 212 L360 205 C430 205 490 230 520 290 Z"/>
      <path class="band" d="M330 0 L400 0 C420 80 410 130 370 180 C340 220 350 255 380 290 L300 290 C280 250 290 215 320 185 C370 135 360 80 330 0 Z"/>
      <path class="spine" role="img" aria-label="Stylised white spine illustration sweeping down the side"
        d="M370 0 L398 0 C412 85 400 135 362 183 C335 220 345 255 372 290 L330 290 C305 250 310 215 338 185 C380 140 385 85 370 0 Z"/>
      <rect class="band" x="0" y="150" width="318" height="60" transform="rotate(2 0 150)"/>
      <g class="service-list" transform="rotate(2 60 170)">
        <path class="tick" d="M60 168 l3 3 l6 -7"/><text x="73" y="172">Private Wheelchair Assessment</text>
        <path class="tick" d="M60 185 l3 3 l6 -7"/><text x="73" y="189">Occupational Therapy</text>
        <path class="tick" d="M60 202 l3 3 l6 -7"/><text x="73" y="206">Wheelchair Skills</text>
      </g>
    </g>
    <rect class="panel-frame" x="10" y="10" width="720" height="270" rx="40"/>
    <text class="brand-name" x="95" y="85" font-size="40">Bramble</text>
    <text class="brand-name" x="97" y="117" font-size="19">Cove Therapy</text>
    <g transform="rotate(4 520 190)">
      <text class="contact contact--small" x="455" y="180">info@bramblecovecare.co.uk</text>
      <text class="contact contact--small" x="455" y="198">bramblecovecare.co.uk</text>
      <text class="contact contact--phone" x="455" y="222">02937 418205</text>
    </g>
  </svg>

  <!-- Rear doors -->
  <svg class="livery-rear" viewBox="0 0 350 310" aria-label="Rear door livery panel">
    <defs>
      <clipPath id="clip-rear"><rect x="10" y="10" width="330" height="290" rx="28"/></clipPath>
    </defs>
    <rect class="panel-fill" x="10" y="10" width="330" height="290" rx="28"/>
    <g clip-path="url(#clip-rear)">
      <rect class="band" x="0" y="200" width="350" height="110"/>
      <path class="band" d="M70 0 L150 0 C120 70 130 120 185 170 C215 200 210 240 170 310 L110 310 C140 250 140 215 110 185 C60 135 50 70 70 0 Z"/>
      <path class="spine" role="img" aria-label="Stylised white spine illustration on the rear doors"
        d="M100 0 L128 0 C105 72 118 122 168 170 C195 198 185 245 145 310 L115 310 C150 250 158 215 128 182 C85 135 80 72 100 0 Z"/>
    </g>
    <rect class="panel-frame" x="10" y="10" width="330" height="290" rx="28"/>
    <text class="brand-name" x="192" y="70" font-size="30">Bramble</text>
    <text class="brand-name" x="194" y="96" font-size="14">Cove Therapy</text>
    <text class="rear-phone" x="205" y="245">02937 418205</text>
  </svg>

</main>
</body>
</html>
```